M&A Advisory firm needs elegant and powerful letterhead

We need a powerful but elegant letterhead to engage with the international financial industry.

Target Market(s)

New York and International Financial Industry

Industry/Entity Type

Finance

Font styles to use
Other font styles liked:
• Poppins

Requirements
Must have
• 482 W 17th Avenue 9th Floor New York, NY 10384 O: +1 (555) 804 2176 F: +1 (555) 804 2193

```html
<!DOCTYPE html>
<html lang="en">
<head>
<meta charset="utf-8">
<title>Corvane Letterhead</title>
<link href="https://fonts.googleapis.com/css2?family=Montserrat:wght@400;600;700&family=Open+Sans:wght@400;600&display=swap" rel="stylesheet">
<style>
  :root {
    --backdrop: #474747;
    --paper: #ffffff;
    --brand-blue: #1f5fa8;
    --rule-blue: #2a66b0;
    --ink-dark: #2b2b2b;
    --ink-mid: #7a7a7a;
    --ink-body: #8a8a8a;
    --signature-tone: #d9d9d9;
  }
  * { margin: 0; padding: 0; box-sizing: border-box; }
  html, body {
    width: 1200px; height: 900px; overflow: hidden;
    background: var(--backdrop);
  }
  .letterhead {
    position: absolute; left: 290px; top: 12px;
    width: 620px; height: 876px;
    background: var(--paper);
    font-family: "Open Sans", sans-serif;
    color: var(--ink-body);
  }
  .brand {
    position: absolute; left: 50px; top: 46px;
    display: flex; align-items: center; gap: 10px;
  }
  .brand-dot {
    width: 14px; height: 14px; border-radius: 50%;
    background: var(--brand-blue);
  }
  .brand-name {
    font-family: "Montserrat", sans-serif; font-weight: 400;
    font-size: 30px; letter-spacing: 1px; color: var(--brand-blue);
  }
  .header-rule {
    position: absolute; left: 200px; right: 50px; top: 92px;
    height: 1px; background: var(--rule-blue);
  }
  .office {
    position: absolute; right: 50px; top: 104px;
    text-align: right; font-size: 8.5px; line-height: 12px;
    color: var(--ink-mid);
  }
  .office .addr { border-bottom: 1px solid var(--rule-blue); padding-bottom: 4px; margin-bottom: 4px; }
  .office .lbl { color: var(--brand-blue); font-weight: 600; }
  .sender {
    position: absolute; left: 50px; top: 130px;
    font-size: 9.5px; line-height: 13px; color: var(--ink-mid);
  }
  .sender .name {
    font-family: "Montserrat", sans-serif; font-weight: 700;
    font-size: 14px; color: var(--ink-dark); margin-bottom: 4px;
  }
  .date {
    position: absolute; right: 50px; top: 240px;
    font-size: 9.5px; color: var(--ink-mid);
  }
  .body-copy {
    position: absolute; left: 50px; top: 272px; width: 520px;
    font-size: 9.5px; line-height: 15px; text-align: justify;
  }
  .body-copy p { margin-bottom: 14px; }
  .sign-off { position: absolute; left: 50px; top: 610px; }
  .signature { width: 150px; height: 34px; background: var(--signature-tone); border-radius: 3px; }
  .sign-off .name {
    font-family: "Montserrat", sans-serif; font-weight: 700;
    font-size: 13px; color: var(--ink-dark); margin-top: 6px; letter-spacing: .5px;
  }
  .sign-off .role { font-size: 9.5px; color: var(--ink-mid); }
  .footer-rule {
    position: absolute; left: 50px; right: 50px; top: 800px;
    height: 1px; background: var(--rule-blue);
  }
</style>
</head>
<body>
  <main class="letterhead">
    <div class="brand">
      <span class="brand-dot"></span>
      <span class="brand-name">CORVANE</span>
    </div>
    <div class="header-rule"></div>

    <address class="office">
      <div class="addr">482 W 17th Avenue<br>9th Floor New York,<br>NY 10384</div>
      <div><span class="lbl">O:</span> +1 (555) 804 2176</div>
      <div><span class="lbl">F:</span> +1 (555) 804 2193</div>
    </address>

    <section class="sender">
      <div class="name">Name Surname</div>
      <div>Senior Executive</div>
      <div>Address goes here, Street, City, Country</div>
      <div>contact@yourmail.com</div>
      <div>000-987-654-321</div>
    </section>

    <div class="date">Date, 10 September, 2030</div>

    <section class="body-copy">
      <p>Lorem ipsum dolor sit amet, consectetur adipisicing elit, sed do eiusmod tempor incididunt ut labore et dolore magna aliqua. Ut enim ad minim veniam, quis nostrud exercitation ullamco laboris nisi ut aliquip ex ea commodo consequat. Duis aute irure dolor in reprehenderit in voluptate velit esse cillum dolore eu fugiat nulla pariatur. Excepteur sint occaecat cupidatat non proident, sunt in culpa qui officia deserunt mollit anim id est laborum. Sed ut perspiciatis unde omnis iste natus error sit voluptatem accusantium doloremque laudantium, totam rem aperiam, eaque ipsa quae ab illo inventore veritatis et quasi architecto beatae vitae dicta sunt explicabo. Nemo enim ipsam voluptatem quia voluptas sit aspernatur aut odit aut fugit, sed quia consequuntur magni dolores eos qui ratione voluptatem sequi nesciunt. Neque porro voluptatem sequi nesciunt. Nemo enim ipsam voluptatem quia voluptas.</p>
      <p>Lorem ipsum dolor sit amet, consectetur adipisicing elit, sed do eiusmod tempor incididunt ut labore et dolore magna aliqua. Ut enim ad minim veniam, quis nostrud exercitation ullamco laboris nisi ut aliquip ex ea commodo consequat. Duis aute irure dolor in reprehenderit in voluptate velit esse cillum dolore eu fugiat nulla pariatur. Excepteur sint occaecat cupidatat non proident, sunt in culpa qui officia deserunt mollit anim id est laborum. Sed ut perspiciatis unde omnis iste natus error sit voluptatem accusantium doloremque laudantium, totam rem aperiam, eaque ipsa quae ab illo inventore veritatis et quasi architecto beatae vitae dicta sunt explicabo. Nemo enim ipsam voluptatem quia voluptas sit aspernatur aut odit aut.</p>
      <p>Lorem ipsum dolor sit amet, consectetur adipisicing elit, sed do eiusmod tempor incididunt ut labore et dolore magna aliqua. Ut enim ad minim veniam, quis nostrud exercitation ullamco laboris nisi ut aliquip ex ea commodo consequat.</p>
    </section>

    <section class="sign-off">
      <div class="signature" role="img" aria-label="Handwritten signature of the general manager"></div>
      <div class="name">NAME SURNAME</div>
      <div class="role">General Manager</div>
    </section>

    <div class="footer-rule"></div>
  </main>
</body>
</html>
```